Unternehmen für Ordnung und Sauberkeit am Arbeitsplatz und Produkte zur Produktionsoptimierung benötigt Visitenkarten und Briefpapier
Zielgruppe
Produkte für Ordnung und Sauberkeit am Arbeitsplatz, Organisation von Arbeitsplätzen, Produkte zur Vereinfachung von Arbeitsabläufen, Produkte zur Produktionsoptimierung unter dem Lean Gedanke, Schlagwort: "5S", nachhaltig, sauber
Aufgabenstellung
Wir sind auf der Suche nach Visitenkarten und Briefpapier für das Unternehmen ourKarto. Nachhaltig, Sauber usw.. Unser Firmenlogo finden Sie anbei.

```html
<!DOCTYPE html>
<html lang="de">
<head>
<meta charset="utf-8">
<title>ourKarto – Briefpapier und Visitenkarten</title>
<link rel="stylesheet" href="https://fonts.googleapis.com/css2?family=Exo+2:ital,wght@0,600;0,700;1,500;1,600;1,700&display=swap">
<style>
:root{
  --backdrop:#1d1d1d;
  --paper:#ffffff;
  --green:#1a9e78;
  --green-soft:#8fd3b8;
  --ink:#4a4a4a;
  --ink-light:#8a8a8a;
  --rule:#b5b5b5;
  --ghost:#ececec;
}
*{margin:0;padding:0;box-sizing:border-box}
html,body{width:1163px;height:1200px;overflow:hidden;background:var(--backdrop)}
body{position:relative;font-family:"Exo 2",sans-serif;color:var(--ink)}
.sheet,.card{position:absolute;background:var(--paper);overflow:hidden;box-shadow:0 4px 14px rgba(0,0,0,.55)}
.swoosh{position:absolute;inset:0;width:100%;height:100%}
.brand{position:absolute;display:flex;align-items:center;gap:8px;font-weight:700;color:var(--green);line-height:1}
.brand-mark{background:var(--green);border-radius:3px}
.web{position:absolute;font-weight:700;font-style:italic;color:var(--ink)}
.it{font-style:italic}

/* letterhead */
.letterhead{left:54px;top:185px;width:706px;height:912px}
.letterhead .brand{left:72px;top:62px;font-size:36px}
.letterhead .brand-mark{width:34px;height:34px}
.letterhead .web{left:168px;top:107px;font-size:14px}
.window-mark{position:absolute;width:18px;height:18px;border-color:var(--rule);border-style:solid;border-width:0}
.wm-tl{left:74px;top:170px;border-left-width:2px;border-top-width:2px}
.wm-tr{left:334px;top:170px;border-right-width:2px;border-top-width:2px}
.wm-bl{left:74px;top:297px;border-left-width:2px;border-bottom-width:2px}
.wm-br{left:334px;top:297px;border-right-width:2px;border-bottom-width:2px}
.sender{position:absolute;left:87px;top:182px;font-size:13px;font-weight:600;font-style:italic;line-height:14px;color:var(--ink)}
.company{color:var(--green);font-weight:700}
.contact-block{position:absolute;right:28px;top:182px;text-align:right;font-size:12.5px;font-style:italic;font-weight:500;line-height:14.5px;color:var(--ink-light)}
.contact-block .company{font-size:13px;margin-bottom:8px}
.contact-block .phones{margin-top:12px;font-style:normal;font-size:11.5px;line-height:13px}
.fold{position:absolute;left:0;width:16px;height:1px;background:var(--rule)}
.fold-1{top:397px}.fold-2{top:706px}
.ghost-brand{position:absolute;left:130px;top:455px;display:flex;align-items:center;gap:18px;font-size:96px;font-weight:700;color:var(--ghost);line-height:1}
.ghost-brand .brand-mark{width:100px;height:100px;background:var(--ghost);border-radius:8px}
.legal{position:absolute;top:857px;display:flex;right:24px}
.legal-col{padding:0 8px;text-align:right;font-size:10.5px;font-style:italic;font-weight:500;line-height:13px;color:var(--ink-light);border-right:1px solid var(--rule);height:38px}
.legal-col:last-child{border-right:none;padding-right:4px}
.legal-col.owner{width:150px}
.legal-col.register{width:196px}
.legal-col.bank{width:212px}

/* business cards */
.card-front{left:796px;top:695px;width:337px;height:188px}
.card-front .brand{right:20px;top:28px;font-size:20px}
.card-front .brand-mark{width:20px;height:20px}
.person{position:absolute;right:21px;top:95px;font-size:13.5px;font-weight:700;font-style:italic;color:var(--green)}
.card-address{position:absolute;right:21px;top:129px;text-align:right;font-size:10.5px;font-weight:600;font-style:italic;line-height:11px}
.card-mail{position:absolute;right:21px;top:163px;font-size:10.5px;font-weight:600;font-style:italic}
.card-phones{position:absolute;left:29px;top:150px;font-size:8.5px;font-weight:600;line-height:14px}
.card-back{left:797px;top:910px;width:336px;height:187px}
.card-back .brand{left:55px;top:68px;font-size:26px}
.card-back .brand-mark{width:26px;height:26px}
.card-back .web{left:126px;top:105px;font-size:10.5px}
</style>
</head>
<body>

<section class="sheet letterhead" aria-label="Briefpapier">
  <svg class="swoosh" viewBox="0 0 706 912" preserveAspectRatio="none" aria-hidden="true">
    <defs>
      <linearGradient id="lhFade" x1="0" y1="0" x2="1" y2="0">
        <stop offset="0" stop-color="#fff" stop-opacity="0"/>
        <stop offset="1" stop-color="#d8d8d8" stop-opacity=".7"/>
      </linearGradient>
    </defs>
    <path d="M300 0 Q560 60 706 260 L706 0 Z" fill="url(#lhFade)"/>
    <path d="M440 0 Q600 40 706 120 L706 70 Q620 20 520 0 Z" fill="var(--green-soft)" opacity=".7"/>
    <path d="M560 0 Q640 60 706 150 L706 110 Q660 40 610 0 Z" fill="#9a9a9a" opacity=".45"/>
    <path d="M500 0 Q620 70 706 200 L706 180 Q630 60 530 0 Z" fill="#bdbdbd" opacity=".5"/>
    <path d="M0 740 Q120 860 330 912 L0 912 Z" fill="#e6e6e6" opacity=".6"/>
    <path d="M0 820 Q100 880 230 912 L140 912 Q60 880 0 850 Z" fill="var(--green-soft)" opacity=".75"/>
    <path d="M0 850 Q80 895 180 912 L120 912 Q50 890 0 870 Z" fill="#9a9a9a" opacity=".45"/>
    <path d="M0 790 Q90 860 240 912 L220 912 Q80 862 0 805 Z" fill="#bdbdbd" opacity=".55"/>
  </svg>

  <div class="brand"><span class="brand-mark"></span><span>ourKarto</span></div>
  <div class="web">www.ourkarto.de</div>

  <span class="window-mark wm-tl"></span><span class="window-mark wm-tr"></span>
  <span class="window-mark wm-bl"></span><span class="window-mark wm-br"></span>

  <address class="sender" style="font-style:italic">
    <div class="company">OURKARTO GbR</div>
    <div>Musterweg 13</div>
    <div>D-65000 Musterstadt</div>
  </address>

  <address class="contact-block">
    <div class="company">OURKARTO GbR</div>
    <div>Musterweg 13</div>
    <div>D-65000 Musterstadt</div>
    <div>Mail: info@ourkarto.de</div>
    <div class="phones">Tel: +49(0)611 – 1234500<br>Fax: +49(0)611 – 1234599</div>
  </address>

  <span class="fold fold-1"></span><span class="fold fold-2"></span>

  <div class="ghost-brand" aria-hidden="true"><span class="brand-mark"></span><span>ourKarto</span></div>

  <footer class="legal">
    <div class="legal-col owner">Inhaber: Max Mustermann<br>Sitz der Gesellschaft:<br>Berlin</div>
    <div class="legal-col register">Eingetragen im Handelsregister<br>Berlin-Charlottenburg<br>HRB 100200 B</div>
    <div class="legal-col bank">Kontorbank Berlin<br>BIC: BBBB DD FF XXX<br>IBAN: DE9900000000000066600</div>
  </footer>
</section>

<section class="card card-front" aria-label="Visitenkarte Vorderseite">
  <svg class="swoosh" viewBox="0 0 337 188" preserveAspectRatio="none" aria-hidden="true">
    <path d="M0 0 L230 0 Q120 30 0 110 Z" fill="#eeeeee"/>
    <path d="M0 40 Q90 0 180 0 L140 0 Q60 10 0 25 Z" fill="var(--green-soft)" opacity=".8"/>
    <path d="M0 70 Q110 10 230 0 L200 0 Q90 15 0 55 Z" fill="#8e8e8e" opacity=".45"/>
    <path d="M0 95 Q60 40 150 10 L120 15 Q50 45 0 85 Z" fill="var(--green)" opacity=".35"/>
    <path d="M0 120 Q80 50 170 20 L160 20 Q70 55 0 112 Z" fill="#b0b0b0" opacity=".5"/>
  </svg>
  <div class="brand"><span class="brand-mark"></span><span>ourKarto</span></div>
  <div class="person">Max Mustermann</div>
  <div class="card-address">Musterweg 13<br>D-65000 Musterstadt</div>
  <div class="card-phones">Tel: +49(0)611 – 1234510<br>Fax: +49(0)611 – 1234590</div>
  <div class="card-mail">Mail: info@ourkarto.de</div>
</section>

<section class="card card-back" aria-label="Visitenkarte Rückseite">
  <svg class="swoosh" viewBox="0 0 336 187" preserveAspectRatio="none" aria-hidden="true">
    <path d="M336 40 Q250 150 120 187 L336 187 Z" fill="#eeeeee"/>
    <path d="M336 90 Q280 160 200 187 L240 187 Q300 160 336 120 Z" fill="var(--green-soft)" opacity=".8"/>
    <path d="M336 60 Q270 150 170 187 L190 187 Q285 150 336 80 Z" fill="#8e8e8e" opacity=".45"/>
    <path d="M336 140 Q310 170 270 187 L310 187 Q325 175 336 165 Z" fill="var(--green)" opacity=".6"/>
  </svg>
  <div class="brand"><span class="brand-mark"></span><span>ourKarto</span></div>
  <div class="web">www.ourkarto.de</div>
</section>

</body>
</html>
```